Packaging for a gift bag make your own dog biscuits.

I am looking for someone who can design me a card design that can be attached to a gift bag containing all the ingredients someone would need in order to make their own dog biscuits. The dog buscuits will be chocolate bone shaped biscuits. My company name is Maple Fern Pantry and i have attached a copy of the company logo to this description. I would like something classy and artisan but not too child like. The design i am looking for is purely the design that will capture the customer all the leagl informastion will be at the back to there is no need to worry about any of this at this stage. The design would need to fit a rectangular or similar shaped piece of card no bigger than 9cm - 14cm I have also attached some pictures of a similar product to give you an idea. The gift bags they will be attached to will be 11cm x 16cm.
The gift bags will be red so it would be nice for the design to compliment this. Ok so just to add a slight complication I am now considering a tent carton as an alternative. I have a picture to a similar type product below. The box I have here is 19cm high (11cm been the square before the tent) 9.5cm width and 7cm girth.

Target Market(s)

Dog lovers, people who visit artisan markets and like to spend time with their much loved fur family.

Font styles to use
Decorative

Colors

Designer to choose colors to be used in the design.

Requirements
Must have
• A classy but artisan design that will attract both adults and kids and may also be something that could be purchased as a gift.
Nice to have
• Something to compliment the red gift bag. The logo visible somewhere on the design and the design in keeping with the company logo.
Should not have
• Any familiar cartoon characters, or a child like feel

```html
<!DOCTYPE html>
<html lang="en">
<head>
<meta charset="utf-8">
<title>Maple Fern Pantry – Chocolate Dog Biscuit Kit Card</title>
<link href="https://fonts.googleapis.com/css2?family=Kaushan+Script&family=Trocchi&family=Didact+Gothic&display=swap" rel="stylesheet">
<style>
  :root {
    --backdrop: #e4e7ea;
    --plank-a: #a9805b;
    --plank-b: #b8926c;
    --plank-c: #9d7552;
    --plank-d: #b08763;
    --plank-seam: #6e4b30;
    --grain: rgba(90, 60, 36, 0.18);
    --paw: rgba(245, 230, 205, 0.28);
    --bone-light: #f6ead2;
    --bone-mid: #ecdcbc;
    --bone-deep: #dcc49a;
    --bone-edge: #7a5232;
    --ink: #5a3a22;
    --ink-soft: #4e3a2c;
    --slot: #c9c4bd;
  }
  * { margin: 0; padding: 0; box-sizing: border-box; }
  html, body {
    width: 1200px;
    height: 923px;
    overflow: hidden;
    background: var(--backdrop);
  }
  .canvas {
    position: relative;
    width: 1200px;
    height: 923px;
  }
  .tag-card {
    position: absolute;
    left: 320px;
    top: 25px;
    width: 560px;
    height: 873px;
    border-radius: 22px;
    overflow: hidden;
    box-shadow: 0 2px 6px rgba(0,0,0,0.18);
  }
  .tag-card svg.card-art {
    position: absolute;
    inset: 0;
  }
  .tag-copy {
    position: absolute;
    inset: 0;
    text-align: center;
    color: var(--ink);
  }
  .brand-name {
    position: absolute;
    top: 176px;
    left: 0;
    right: 0;
    font-family: "Trocchi", serif;
    font-size: 26px;
    color: var(--ink);
  }
  .flavour {
    position: absolute;
    top: 294px;
    left: 0;
    right: 0;
    font-family: "Kaushan Script", cursive;
    font-weight: 400;
    font-size: 80px;
    line-height: 1;
    color: var(--ink);
    transform: scaleX(0.72);
    transform-origin: 280px 50%;
    white-space: nowrap;
  }
  .product-title {
    position: absolute;
    top: 388px;
    left: 0;
    right: 0;
    font-family: "Trocchi", serif;
    font-weight: 400;
    font-size: 50px;
    line-height: 50px;
    color: var(--ink);
  }
  .contents-heading {
    position: absolute;
    top: 566px;
    left: 0;
    right: 0;
    font-family: "Didact Gothic", sans-serif;
    font-weight: 400;
    font-size: 32px;
    color: var(--ink);
  }
  .contents-heading span {
    text-decoration: underline;
    text-decoration-thickness: 2px;
    text-underline-offset: 5px;
  }
  .contents-note {
    position: absolute;
    top: 610px;
    left: 0;
    right: 0;
    font-family: "Didact Gothic", sans-serif;
    font-size: 25px;
    line-height: 31px;
    color: var(--ink-soft);
  }
</style>
</head>
<body>
<main class="canvas">
  <article class="tag-card">
    <svg class="card-art" width="560" height="873" viewBox="0 0 560 873" xmlns="http://www.w3.org/2000/svg">
      <defs>
        <linearGradient id="boneTone" x1="0" y1="0" x2="1" y2="0">
          <stop offset="0" stop-color="var(--bone-deep)"/>
          <stop offset="0.35" stop-color="var(--bone-light)"/>
          <stop offset="0.7" stop-color="var(--bone-mid)"/>
          <stop offset="1" stop-color="var(--bone-deep)"/>
        </linearGradient>
        <linearGradient id="plankShade" x1="0" y1="0" x2="1" y2="0">
          <stop offset="0" stop-color="rgba(0,0,0,0.06)"/>
          <stop offset="0.5" stop-color="rgba(255,255,255,0.05)"/>
          <stop offset="1" stop-color="rgba(0,0,0,0.12)"/>
        </linearGradient>
      </defs>

      <g class="wood-planks">
        <rect x="0" y="0" width="62" height="873" fill="var(--plank-a)"/>
        <rect x="62" y="0" width="70" height="873" fill="var(--plank-b)"/>
        <rect x="132" y="0" width="68" height="873" fill="var(--plank-c)"/>
        <rect x="200" y="0" width="72" height="873" fill="var(--plank-d)"/>
        <rect x="272" y="0" width="70" height="873" fill="var(--plank-a)"/>
        <rect x="342" y="0" width="68" height="873" fill="var(--plank-b)"/>
        <rect x="410" y="0" width="72" height="873" fill="var(--plank-c)"/>
        <rect x="482" y="0" width="78" height="873" fill="var(--plank-d)"/>
        <rect x="0" y="0" width="560" height="873" fill="url(#plankShade)"/>
        <g stroke="var(--plank-seam)" stroke-width="2" opacity="0.55">
          <line x1="62" y1="0" x2="62" y2="873"/>
          <line x1="132" y1="0" x2="132" y2="873"/>
          <line x1="200" y1="0" x2="200" y2="873"/>
          <line x1="272" y1="0" x2="272" y2="873"/>
          <line x1="342" y1="0" x2="342" y2="873"/>
          <line x1="410" y1="0" x2="410" y2="873"/>
          <line x1="482" y1="0" x2="482" y2="873"/>
        </g>
        <g stroke="var(--grain)" stroke-width="1.2" fill="none">
          <line x1="22" y1="0" x2="24" y2="873"/>
          <line x1="44" y1="0" x2="42" y2="873"/>
          <line x1="90" y1="0" x2="92" y2="873"/>
          <line x1="112" y1="0" x2="110" y2="873"/>
          <line x1="440" y1="0" x2="442" y2="873"/>
          <line x1="462" y1="0" x2="460" y2="873"/>
          <line x1="508" y1="0" x2="510" y2="873"/>
          <line x1="536" y1="0" x2="534" y2="873"/>
        </g>
      </g>

      <g class="paw-print-areas" role="img" aria-label="Faint paw prints on the wood">
        <ellipse cx="40" cy="95" rx="42" ry="38" fill="var(--paw)"/>
        <ellipse cx="505" cy="470" rx="52" ry="46" fill="var(--paw)"/>
        <ellipse cx="55" cy="720" rx="46" ry="42" fill="var(--paw)"/>
      </g>

      <rect class="hang-slot" x="235" y="24" width="88" height="11" rx="5.5" fill="var(--slot)"/>
      <path class="bone-shadow" transform="translate(9 7)" fill="var(--bone-edge)"
        d="M280 72 C240 40 200 25 160 30 C100 38 80 90 95 140 C105 180 140 210 150 240 L150 620 C140 660 90 690 85 760 C82 830 130 870 185 860 C230 850 255 820 280 815 C305 820 330 850 375 860 C430 870 478 830 475 760 C470 690 420 660 410 620 L410 240 C420 210 455 180 465 140 C480 90 460 38 400 30 C360 25 320 40 280 72 Z"/>
      <path class="bone-panel" fill="url(#boneTone)"
        d="M280 72 C240 40 200 25 160 30 C100 38 80 90 95 140 C105 180 140 210 150 240 L150 620 C140 660 90 690 85 760 C82 830 130 870 185 860 C230 850 255 820 280 815 C305 820 330 850 375 860 C430 870 478 830 475 760 C470 690 420 660 410 620 L410 240 C420 210 455 180 465 140 C480 90 460 38 400 30 C360 25 320 40 280 72 Z"/>
    </svg>
    <div class="tag-copy">
      <p class="brand-name">Maple Fern Pantry</p>
      <h1 class="flavour">Chocolate</h1>
      <h2 class="product-title">Dog<br>Biscuit<br>Kit</h2>
      <h3 class="contents-heading"><span>In The Bag</span></h3>
      <p class="contents-note">List of ingredients<br>that’s in the bag.<br>Everything needed<br>to make the dog<br>biscuits.</p>
    </div>
  </article>
</main>
</body>
</html>
```